you will use Ai to Copy the website Quellabyx.com to come up with the basic frame work and it will give you the understanding of how I would like Zandoprik.com to be like. Zandoprik.com is a peer to peer rv rental site very similar to both of the other rv rental sites the difference is that are commission based 20% and above per rental and we will be one flat monthly rate and they keep all the earnings. Below is photo that will help you with the color scheme and the look and feel of the design

```html
<!DOCTYPE html>
<html lang="en">
<head>
<meta charset="utf-8">
<title>Zandoprik.com — Peer-to-Peer RV Rentals</title>
<link href="https://fonts.googleapis.com/css2?family=Poppins:wght@500;600;700;800&family=Inter:wght@400;500;600;700&display=swap" rel="stylesheet">
<style>
:root{
  --green:#5c9b33;
  --green-dark:#4a8227;
  --green-soft:#eef5e7;
  --navy:#0f1826;
  --navy-2:#1a2433;
  --ink:#151c26;
  --muted:#6b7280;
  --line:#e5e7eb;
  --bg-soft:#f4f5f4;
  --white:#ffffff;
  --star:#e8a23a;
}
*{box-sizing:border-box;margin:0;padding:0}
html,body{width:1200px;height:5391px;overflow:hidden}
body{font-family:"Inter",sans-serif;color:var(--ink);background:var(--white);font-size:11px;line-height:1.5}
h1,h2,h3,h4,.display{font-family:"Poppins",sans-serif}
.wrap{width:802px;margin:0 auto;position:relative}
.eyebrow{display:inline-block;font-size:7.5px;font-weight:700;letter-spacing:.09em;text-transform:uppercase;color:var(--green-dark);background:var(--green-soft);padding:3px 8px;border-radius:20px}
.center{text-align:center}
.sec-title{font-size:22px;font-weight:700;line-height:1.22;letter-spacing:-.02em;margin-top:8px}
.sec-sub{color:var(--muted);font-size:11.5px;margin-top:10px}
.btn{display:inline-flex;align-items:center;gap:6px;font-weight:600;font-size:9.5px;border-radius:20px;padding:7px 16px;border:1.5px solid transparent;white-space:nowrap}
.btn-green{background:var(--green);color:#fff}
.btn-outline{border-color:var(--green);color:var(--green)}
.btn-ghost{border-color:#fff;color:#fff}
.ph{display:block}
.check{color:var(--green)}

/* hero */
.hero{height:497px;position:relative;background:linear-gradient(100deg,#252c36 0%,#39404a 45%,#6e6a63 75%,#8d8477 100%);color:#fff}
.hero .ph{position:absolute;inset:0;background:linear-gradient(180deg,rgba(20,26,36,.55),rgba(20,26,36,.35) 60%,rgba(30,30,30,.6))}
.nav{position:absolute;top:14px;left:220px;right:220px;display:flex;align-items:center;height:32px}
.logo{font-family:"Poppins",sans-serif;font-weight:700;font-size:19px;color:#fff;line-height:1}
.nav-links{display:flex;gap:18px;margin-left:48px;font-size:9px;font-weight:500}
.nav-right{margin-left:auto;display:flex;align-items:center;gap:14px;font-size:9px}
.hero-copy{position:absolute;left:220px;top:130px;width:520px}
.hero-copy .eyebrow{background:rgba(255,255,255,.14);color:#fff}
.hero-copy h1{font-size:38px;line-height:1.02;font-weight:800;letter-spacing:-.03em;margin-top:10px}
.hero-copy p{font-size:11.5px;margin-top:14px;width:360px;opacity:.9}
.search{position:absolute;left:220px;top:318px;width:760px;height:63px;background:#fff;border-radius:8px;display:flex;align-items:flex-end;padding:0 12px 12px;gap:12px;color:var(--ink)}
.field{display:flex;flex-direction:column;gap:4px}
.field label{font-size:6.5px;font-weight:700;letter-spacing:.06em;text-transform:uppercase}
.field span{border:1px solid var(--line);border-radius:5px;height:24px;display:flex;align-items:center;padding:0 8px;font-size:9px;color:#9ca3af;justify-content:space-between}
.search .btn{height:26px}
.owner-note{position:absolute;left:220px;top:394px;font-size:8.5px;opacity:.9}
.owner-note b{color:#8fcf5e;font-weight:600}
.stats{position:absolute;left:258px;top:444px;width:682px;height:84px;background:#fff;border-radius:10px;box-shadow:0 10px 30px rgba(0,0,0,.12);display:flex;align-items:center;z-index:2}
.stat{flex:1;text-align:center;border-right:1px solid var(--line)}
.stat:last-child{border:0}
.stat b{display:block;font-family:"Poppins",sans-serif;font-size:22px;color:var(--green-dark);font-weight:700;line-height:1.1}
.stat span{font-size:7.5px;color:var(--ink);font-weight:500}

/* how */
.how{height:462px;padding-top:103px}
.steps{display:flex;justify-content:space-between;margin-top:54px}
.step{width:220px;text-align:center}
.step .ic{width:34px;height:34px;border-radius:8px;background:var(--green-soft);display:inline-flex;align-items:center;justify-content:center}
.step small{display:block;color:var(--green-dark);font-weight:700;font-size:7.5px;letter-spacing:.08em;margin-top:6px}
.step h3{font-size:12px;font-weight:700;margin-top:2px}
.step p{color:var(--muted);font-size:9.5px;margin-top:4px}

/* two ways */
.ways{height:616px;background:var(--bg-soft);padding-top:72px}
.ways-cards{display:flex;gap:19px;margin-top:36px}
.way{flex:1;border-radius:8px;overflow:hidden;height:369px;background:#fff;box-shadow:0 2px 10px rgba(0,0,0,.05)}
.way .ph{height:162px}
.way .body{padding:18px 20px}
.way h3{font-size:14px;font-weight:700}
.way p{color:var(--muted);font-size:9.5px;margin-top:8px}
.way ul{list-style:none;margin-top:10px}
.way li{font-size:8.5px;margin-bottom:5px;display:flex;gap:7px;color:#4b5563}
.way .btn{margin-top:10px}
.way.dark{background:var(--navy);color:#fff}
.way.dark p,.way.dark li{color:#c9ced6}

/* fit */
.fit{height:460px;padding-top:74px}
.fit-cards{display:flex;gap:14px;margin-top:40px}
.rig{flex:1;border:1px solid var(--line);border-radius:7px;overflow:hidden;height:190px}
.rig .ph{height:120px;position:relative}
.tag{position:absolute;top:8px;left:8px;background:#fff;color:var(--ink);font-size:6.5px;font-weight:600;padding:2px 6px;border-radius:10px}
.rig .body{padding:10px 12px}
.rig h4{font-size:10.5px;font-weight:700}
.rig p{font-size:7.5px;color:var(--muted);margin-top:3px;line-height:1.45}

/* flat fee */
.fee{height:478px;background:var(--navy);color:#fff;padding-top:74px}
.fee .eyebrow{background:rgba(92,155,51,.2);color:#8fcf5e}
.fee .sec-sub{color:#c1c7d0;width:420px;margin:12px auto 0}
.compare{display:flex;gap:17px;margin-top:40px}
.box{flex:1;border-radius:8px;padding:22px 20px;height:166px}
.box.old{background:var(--navy-2);border:1px solid #2a3546}
.box.new{background:var(--green)}
.box small{font-size:7px;letter-spacing:.1em;font-weight:700;text-transform:uppercase;opacity:.7}
.box .big{font-family:"Poppins",sans-serif;font-size:21px;font-weight:700;margin-top:4px}
.box .big span{font-size:10px;font-weight:500;font-family:"Inter",sans-serif}
.box ul{list-style:none;margin-top:12px}
.box li{font-size:8.5px;margin-bottom:9px;display:flex;gap:8px}
.box.old li{color:#aab2be}

/* owners */
.owners{height:523px;padding-top:74px}
.owners-grid{display:flex;gap:42px}
.owners-text{width:380px}
.owners-text .sec-title{font-size:21px}
.owners-text>p{color:var(--muted);font-size:10.5px;margin-top:10px}
.perks{list-style:none;margin-top:16px}
.perks li{display:flex;gap:10px;margin-bottom:10px}
.perks .ic{width:16px;height:16px;border-radius:50%;background:var(--green-soft);flex:none;display:flex;align-items:center;justify-content:center}
.perks b{display:block;font-size:9px}
.perks span{font-size:7.5px;color:var(--muted)}
.owners-cta{display:flex;align-items:center;gap:12px;margin-top:6px;font-size:8px;color:var(--muted)}
.owners-photo{position:relative;width:382px;margin-top:42px}
.owners-photo .ph{height:254px;border-radius:8px}
.earn{position:absolute;left:-8px;bottom:-26px;background:#fff;border-radius:6px;padding:8px 14px;box-shadow:0 6px 20px rgba(0,0,0,.12)}
.earn small{font-size:6.5px;font-weight:700;letter-spacing:.08em;color:var(--muted)}
.earn b{display:block;font-family:"Poppins",sans-serif;color:var(--green-dark);font-size:17px;line-height:1.1}
.earn b span{font-size:9px;color:var(--muted);font-weight:500}
.footnote{font-size:7px;color:#9ca3af;margin-top:22px}

/* popular */
.popular{height:465px;background:var(--bg-soft);padding-top:82px}
.pop-cards{display:flex;gap:21px;margin-top:32px}
.pop{flex:1;background:#fff;border-radius:8px;overflow:hidden;height:237px;box-shadow:0 2px 10px rgba(0,0,0,.05)}
.pop .ph{height:142px;position:relative}
.pop .tag{background:var(--green);color:#fff}
.pop .body{padding:12px 14px}
.pop .row{display:flex;justify-content:space-between;align-items:center}
.pop h4{font-size:11px;font-weight:700}
.pop .rate{color:var(--star);font-size:8px;font-weight:600}
.pop .meta{font-size:7.5px;color:var(--muted)}
.pop .price{font-family:"Poppins",sans-serif;font-weight:700;font-size:13px}
.pop .price span{font-size:8px;color:var(--muted);font-weight:500;font-family:"Inter",sans-serif}
.pop .link{color:var(--green-dark);font-size:8px;font-weight:600}
.pop .row.bottom{margin-top:12px}

/* peace */
.peace{height:524px;padding-top:71px}
.peace-grid{display:flex;gap:42px;align-items:center}
.peace-text{width:378px}
.peace-text .sec-title{font-size:21px}
.peace-text>p{color:var(--muted);font-size:10.5px;margin-top:10px}
.features{display:grid;grid-template-columns:1fr 1fr;gap:22px 24px;margin-top:24px}
.feat .ic{width:18px;height:18px;border-radius:5px;background:var(--green-soft);display:flex;align-items:center;justify-content:center}
.feat b{display:block;font-size:9px;margin-top:6px}
.feat span{font-size:7.5px;color:var(--muted)}
.peace-photo{width:382px;height:381px;border-radius:8px}

/* testimonials */
.reviews{height:431px;background:var(--bg-soft);padding-top:77px}
.rev-cards{display:flex;gap:21px;margin-top:34px}
.rev{flex:1;background:#fff;border-radius:8px;padding:20px;height:182px;box-shadow:0 2px 10px rgba(0,0,0,.04)}
.stars{color:var(--star);font-size:10px;letter-spacing:1px}
.rev p{font-size:9px;color:#4b5563;margin-top:8px;line-height:1.55}
.who{display:flex;align-items:center;gap:8px;margin-top:12px}
.avatar{width:24px;height:24px;border-radius:50%;background:#5d6370}
.who b{font-size:8.5px;display:block}
.who span{font-size:7px;color:var(--muted)}

/* faq */
.faq{height:448px;padding-top:52px}
.faq-list{width:478px;margin:30px auto 0}
.faq-item{display:flex;justify-content:space-between;align-items:center;height:36px;border:1px solid var(--line);border-radius:6px;padding:0 14px;margin-bottom:8px;font-size:9px;font-weight:600}

/* cta */
.cta{height:226px;background:linear-gradient(180deg,#1c2632,#141d29);color:#fff;text-align:center;padding-top:58px;position:relative;overflow:hidden}
.cta h2{font-size:22px;font-weight:700;letter-spacing:-.02em}
.cta p{font-size:10.5px;color:#c9ced6;width:470px;margin:10px auto 0}
.cta .btns{display:flex;gap:10px;justify-content:center;margin-top:20px}

/* footer */
footer{height:261px;background:var(--navy);color:#c1c7d0;padding-top:60px}
.foot-top{display:flex}
.foot-brand{width:254px}
.foot-brand .logo{font-size:17px}
.foot-brand p{font-size:7.5px;margin-top:10px;width:200px}
.socials{display:flex;gap:8px;margin-top:14px}
.socials i{width:16px;height:16px;border-radius:50%;background:#2a3546;display:block}
.foot-col{width:114px}
.foot-col h5,.news h5{font-size:7.5px;color:#fff;letter-spacing:.08em;font-weight:700;text-transform:uppercase;margin-bottom:8px;font-family:"Inter",sans-serif}
.foot-col a{display:block;font-size:8px;margin-bottom:6px;color:#aab2be;text-decoration:none}
.news{width:195px}
.news p{font-size:7.5px}
.news .form{display:flex;gap:6px;margin-top:10px}
.news .form span{flex:1;height:22px;border-radius:4px;background:#1f2a3a;font-size:7.5px;display:flex;align-items:center;padding:0 8px;color:#7a8492}
.news .form b{background:var(--green);color:#fff;font-size:7.5px;padding:0 10px;border-radius:4px;display:flex;align-items:center}
.foot-bottom{display:flex;justify-content:space-between;border-top:1px solid #222d3c;margin-top:42px;padding-top:12px;font-size:7.5px;color:#8a94a2}
.foot-bottom div{display:flex;gap:16px}
</style>
</head>
<body>

<header class="hero">
  <div class="ph" role="img" aria-label="Motorhome parked on a hillside at dusk under a cloudy sky"></div>
  <nav class="nav">
    <div class="logo">Zandoprik.com</div>
    <div class="nav-links"><span>How It Works</span><span>Find an RV</span><span>List Your RV</span><span>Why Us</span><span>Reviews</span><span>FAQ</span></div>
    <div class="nav-right"><span>Log In</span><span class="btn btn-green">List Your RV</span></div>
  </nav>
  <div class="hero-copy">
    <span class="eyebrow">Peer-to-peer RV rentals, reinvented</span>
    <h1>Your Next Great Escape Is Parked A Few Miles Away</h1>
    <p>Zandoprik connects road-trippers with real RV owners in their own neighborhood — browse motorhomes, campers, and trailers nationwide, and skip the corporate mark-up.</p>
  </div>
  <div class="search">
    <div class="field" style="width:230px"><label>Where to?</label><span>City, state, or zip</span></div>
    <div class="field" style="width:140px"><label>Pick up</label><span>dd-mm-yyyy <svg width="8" height="8" viewBox="0 0 8 8"><rect x=".5" y="1" width="7" height="6.5" rx="1" fill="none" stroke="#555"/></svg></span></div>
    <div class="field" style="width:140px"><label>Return</label><span>dd-mm-yyyy <svg width="8" height="8" viewBox="0 0 8 8"><rect x=".5" y="1" width="7" height="6.5" rx="1" fill="none" stroke="#555"/></svg></span></div>
    <div class="field" style="width:118px"><label>RV Type</label><span style="color:var(--ink)">Any Type <svg width="7" height="5" viewBox="0 0 7 5"><path d="M.5 .5l3 3 3-3" fill="none" stroke="#555"/></svg></span></div>
    <span class="btn btn-green"><svg width="9" height="9" viewBox="0 0 10 10"><circle cx="4" cy="4" r="3" fill="none" stroke="#fff" stroke-width="1.4"/><path d="M6.3 6.3L9 9" stroke="#fff" stroke-width="1.4"/></svg>Search</span>
  </div>
  <div class="owner-note">Own an RV instead? <b>List it and keep 100% of your earnings →</b></div>
  <div class="stats">
    <div class="stat"><b>12,400+</b><span>RVs Listed Nationwide</span></div>
    <div class="stat"><b>48,000+</b><span>Trips Booked &amp; Counting</span></div>
    <div class="stat"><b>100%</b><span>Of Earnings Owners Keep</span></div>
    <div class="stat"><b>4.9/5</b><span>Average Renter Rating</span></div>
  </div>
</header>

<section class="how">
  <div class="wrap center">
    <span class="eyebrow">How it works</span>
    <h2 class="sec-title">Getting Away Is Simpler Than You<br>Think</h2>
    <p class="sec-sub">Three steps between you and a campsite sunset — no dealership, no lease, no<br>hassle.</p>
    <div class="steps">
      <div class="step"><span class="ic"><svg width="14" height="14" viewBox="0 0 14 14"><circle cx="6" cy="6" r="4" fill="none" stroke="#5c9b33" stroke-width="1.5"/><path d="M9 9l3.5 3.5" stroke="#5c9b33" stroke-width="1.5"/></svg></span><small>STEP 01</small><h3>Search &amp; Compare</h3><p>Browse verified RVs by type, location, and dates. Filter for pet-friendly rigs, solar power, full kitchens, and more.</p></div>
      <div class="step"><span class="ic"><svg width="14" height="14" viewBox="0 0 14 14"><circle cx="7" cy="7" r="5.5" fill="none" stroke="#5c9b33" stroke-width="1.4"/><path d="M4.5 7l2 2 3-3.5" fill="none" stroke="#5c9b33" stroke-width="1.4"/></svg></span><small>STEP 02</small><h3>Book With Confidence</h3><p>Message the owner, lock in your dates, and travel knowing every trip includes protection coverage and 24/7 roadside support.</p></div>
      <div class="step"><span class="ic"><svg width="14" height="14" viewBox="0 0 14 14"><rect x="2" y="2" width="10" height="10" rx="2" fill="none" stroke="#5c9b33" stroke-width="1.4"/><path d="M5 7h4M7 5v4" stroke="#5c9b33" stroke-width="1.4"/></svg></span><small>STEP 03</small><h3>Hit The Road</h3><p>Pick up (or get it delivered), run through a quick walkthrough, and go make memories. Return it full and rested.</p></div>
    </div>
  </div>
</section>

<section class="ways">
  <div class="wrap">
    <div class="center"><span class="eyebrow">Two ways to ride with us</span>
    <h2 class="sec-title">Whether You're Renting Or Listing, We<br>Built This For You</h2></div>
    <div class="ways-cards">
      <div class="way">
        <div class="ph" role="img" aria-label="Class C motorhome parked on grass with a family nearby" style="background:linear-gradient(180deg,#9fb4c2,#c9c5b6 55%,#6f7d4d)"></div>
        <div class="body">
          <h3>Find Your Rig</h3>
          <p>Thousands of verified RVs, real owner reviews, and transparent all-in pricing — no surprise fees at checkout.</p>
          <ul><li><span class="check">✓</span>Thousands of verified listings nationwide</li><li><span class="check">✓</span>Transparent, all-in pricing — no hidden fees</li><li><span class="check">✓</span>24/7 roadside assistance on every trip</li></ul>
          <span class="btn btn-outline">Browse RVs</span>
        </div>
      </div>
      <div class="way dark">
        <div class="ph" role="img" aria-label="Motorhome parked on a red desert road" style="background:linear-gradient(180deg,#c8d6e2,#d5b690 55%,#9a5a38)"></div>
        <div class="body">
          <h3>List Your RV</h3>
          <p>Turn idle weekends into real income — with one flat monthly fee instead of a cut of every booking.</p>
          <ul><li><span class="check">✓</span>Keep 100% of your rental income</li><li><span class="check">✓</span>One flat monthly fee — no per-booking commission</li><li><span class="check">✓</span>Set your own price, calendar &amp; house rules</li></ul>
          <span class="btn btn-green">Start Earning</span>
        </div>
      </div>
    </div>
  </div>
</section>

<section class="fit">
  <div class="wrap">
    <div class="center"><span class="eyebrow">Find your fit</span>
    <h2 class="sec-title">Every Kind Of Rig, All In One Place</h2>
    <p class="sec-sub">From full-size land yachts to nimble camper vans — filter by the type that<br>matches your trip.</p></div>
    <div class="fit-cards">
      <div class="rig"><div class="ph" role="img" aria-label="Class A motorhome" style="background:linear-gradient(180deg,#b9c7d3,#ddd6c7 60%,#8c8a6b)"><span class="tag">From $189/night</span></div><div class="body"><h4>Class A Motorhomes</h4><p>The full-size land yacht — room for the whole family, and then some.</p></div></div>
      <div class="rig"><div class="ph" role="img" aria-label="Class C motorhome in a forest" style="background:linear-gradient(180deg,#3c4a3f,#6b7566 60%,#2f3a30)"><span class="tag">From $129/night</span></div><div class="body"><h4>Class C Motorhomes</h4><p>Easy to drive, comfortable to live in — the RV world favorite.</p></div></div>
      <div class="rig"><div class="ph" role="img" aria-label="Travel trailer at a campsite" style="background:linear-gradient(180deg,#a9c1d6,#e2dcd0 60%,#b08b6a)"><span class="tag">From $89/night</span></div><div class="body"><h4>Travel Trailers</h4><p>Tow it with your own truck and park it wherever the view is best.</p></div></div>
      <div class="rig"><div class="ph" role="img" aria-label="Camper van in the desert" style="background:linear-gradient(180deg,#c4d2de,#c9a47f 60%,#8a5638)"><span class="tag">From $79/night</span></div><div class="body"><h4>Camper Vans</h4><p>Nimble, fuel-efficient, and always ready for the backroads.</p></div></div>
    </div>
  </div>
</section>

<section class="fee">
  <div class="wrap">
    <div class="center"><span class="eyebrow">The Zandoprik difference</span>
    <h2 class="sec-title">One Flat Fee. Zero Commission. All<br>Yours.</h2>
    <p class="sec-sub">Most peer-to-peer RV marketplaces take 20% or more of every booking before an owner sees a dime. We think that's backwards — you own the rig and take the risk, so you should keep the reward.</p></div>
    <div class="compare">
      <div class="box old"><small>Other RV marketplaces</small><div class="big">20%+ <span>per booking</span></div>
        <ul><li>✕ Commission taken out of every single trip</li><li>✕ Earnings shrink the more you rent it out</li><li>✕ Platform sets many of the rules</li></ul></div>
      <div class="box new"><small>Zandoprik</small><div class="big">Flat Monthly Fee</div>
        <ul><li>✓ Keep 100% of every booking, always</li><li>✓ One predictable price, no matter how much you earn</li><li>✓ You set your own price &amp; policies</li></ul></div>
    </div>
  </div>
</section>

<section class="owners">
  <div class="wrap">
    <div class="owners-grid">
      <div class="owners-text">
        <span class="eyebrow">For RV owners</span>
        <h2 class="sec-title">Turn Idle Weekends Into Real<br>Income</h2>
        <p>Your RV spends most of the year parked in the driveway. List it on Zandoprik and put it to work — without handing a chunk of every trip to a middleman.</p>
        <ul class="perks">
          <li><span class="ic"><svg width="8" height="8" viewBox="0 0 8 8"><path d="M1.5 4l1.7 1.7L6.5 2.3" fill="none" stroke="#5c9b33" stroke-width="1.2"/></svg></span><div><b>Flat monthly fee, no commission — ever</b><span>Pay one predictable price and keep every dollar you earn from every trip.</span></div></li>
          <li><span class="ic"><svg width="8" height="8" viewBox="0 0 8 8"><rect x="1" y="1.5" width="6" height="5.5" rx="1" fill="none" stroke="#5c9b33"/></svg></span><div><b>Choose your own renters, price &amp; calendar</b><span>You decide who books, what nights are open, and what you charge.</span></div></li>
          <li><span class="ic"><svg width="8" height="8" viewBox="0 0 8 8"><path d="M4 .8l2.7 1v2.2C6.7 5.8 4 7.2 4 7.2S1.3 5.8 1.3 4V1.8z" fill="none" stroke="#5c9b33"/></svg></span><div><b>$1M owner protection plan included</b><span>Every listing is backed by comprehensive liability coverage, at no extra cost.</span></div></li>
          <li><span class="ic"><svg width="8" height="8" viewBox="0 0 8 8"><circle cx="4" cy="4" r="2.8" fill="none" stroke="#5c9b33"/></svg></span><div><b>Real support, seven days a week</b><span>A dedicated owner-support team is on call whenever you need a hand.</span></div></li>
        </ul>
        <div class="owners-cta"><span class="btn btn-green">List Your RV — Free To Start</span>No credit card required to get listed.</div>
      </div>
      <div class="owners-photo">
        <div class="ph" role="img" aria-label="Class C motorhome parked at a lakeside camp" style="background:linear-gradient(180deg,#cfd9de,#e3ddd0 50%,#8a8a6c)"></div>
        <div class="earn"><small>AVG. OWNER KEEPS</small><b>$650<span>/mo more*</span></b></div>
      </div>
    </div>
    <p class="footnote">*Estimated additional monthly earnings versus a 20% commission-based platform, based on average booking volume across active Zandoprik owner accounts.</p>
  </div>
</section>

<section class="popular">
  <div class="wrap">
    <div class="center"><span class="eyebrow">Fresh off the lot</span>
    <h2 class="sec-title">Popular Rigs Ready For Booking</h2></div>
    <div class="pop-cards">
      <div class="pop"><div class="ph" role="img" aria-label="Warm-lit RV interior with a dinette" style="background:linear-gradient(160deg,#3a2418,#a8683a 55%,#5a3826)"><span class="tag">Pet Friendly</span></div><div class="body"><div class="row"><h4>The Driftlodge</h4><span class="rate">★ 4.9</span></div><div class="meta">Class C Motorhome · Bend, OR</div><div class="row bottom"><span class="price">$159<span>/night</span></span><span class="link">View Details →</span></div></div></div>
      <div class="pop"><div class="ph" role="img" aria-label="Bright RV interior with red cabinetry" style="background:linear-gradient(160deg,#6a4a3a,#d6c4aa 55%,#8c3c30)"><span class="tag">Sleeps 6</span></div><div class="body"><div class="row"><h4>Basecamp Bertha</h4><span class="rate">★ 5.0</span></div><div class="meta">Travel Trailer · Asheville, NC</div><div class="row bottom"><span class="price">$95<span>/night</span></span><span class="link">View Details →</span></div></div></div>
      <div class="pop"><div class="ph" role="img" aria-label="Cozy camper van interior with wood paneling" style="background:linear-gradient(160deg,#4a2c1a,#b87844 55%,#6a4026)"><span class="tag">Solar Powered</span></div><div class="body"><div class="row"><h4>The Rambler</h4><span class="rate">★ 4.8</span></div><div class="meta">Camper Van · Flagstaff, AZ</div><div class="row bottom"><span class="price">$135<span>/night</span></span><span class="link">View Details →</span></div></div></div>
    </div>
  </div>
</section>

<section class="peace">
  <div class="wrap">
    <div class="peace-grid">
      <div class="peace-text">
        <span class="eyebrow">Peace of mind, included</span>
        <h2 class="sec-title">Every Trip Is Backed, Every Time</h2>
        <p>Renting or lending your rig to a stranger shouldn't feel like a gamble. Here's what's automatically included.</p>
        <div class="features">
          <div class="feat"><span class="ic"><svg width="9" height="9" viewBox="0 0 10 10"><circle cx="5" cy="5" r="4" fill="none" stroke="#5c9b33"/><path d="M3 5l1.5 1.5L7 3.8" fill="none" stroke="#5c9b33"/></svg></span><b>Verified Members</b><span>ID and license verification for every renter and owner before booking.</span></div>
          <div class="feat"><span class="ic"><svg width="9" height="9" viewBox="0 0 10 10"><rect x="2" y="4.5" width="6" height="4.5" rx="1" fill="none" stroke="#5c9b33"/><path d="M3.3 4.5V3a1.7 1.7 0 013.4 0v1.5" fill="none" stroke="#5c9b33"/></svg></span><b>$1M Protection Plan</b><span>Comprehensive liability coverage included on every single booking.</span></div>
          <div class="feat"><span class="ic"><svg width="9" height="9" viewBox="0 0 10 10"><path d="M5 1v8M1 5h8M2.2 2.2l5.6 5.6M7.8 2.2L2.2 7.8" stroke="#5c9b33"/></svg></span><b>24/7 Roadside Support</b><span>Flat tires, dead batteries, and locked-out moments — handled fast.</span></div>
          <div class="feat"><span class="ic"><svg width="9" height="9" viewBox="0 0 10 10"><rect x="1" y="2" width="8" height="6" rx="1" fill="none" stroke="#5c9b33"/><path d="M1 4h8" stroke="#5c9b33"/></svg></span><b>Secure Payments</b><span>Funds are held safely and released 24 hours after every trip begins.</span></div>
        </div>
      </div>
      <div class="peace-photo ph" role="img" aria-label="Friends sharing an evening laugh beside a camper van at dusk" style="background:radial-gradient(circle at 40% 55%,#b36a3a,#4a2a1c 55%,#1e1c24)"></div>
    </div>
  </div>
</section>

<section class="reviews">
  <div class="wrap">
    <div class="center"><span class="eyebrow">Real trips, real people</span>
    <h2 class="sec-title">What The Pack Is Saying</h2></div>
    <div class="rev-cards">
      <div class="rev"><div class="stars">★★★★★</div><p>"We booked a Class C for a week in the Tetons and the whole process took ten minutes. Way cheaper than the big rental chains, and the owner left us a full guide to the rig."</p><div class="who"><span class="avatar"></span><div><b>Jordan T.</b><span>Renter · Austin, TX</span></div></div></div>
      <div class="rev"><div class="stars">★★★★★</div><p>"I switched over from a commission platform and I'm keeping hundreds more every month for the exact same bookings. The flat fee just makes sense."</p><div class="who"><span class="avatar"></span><div><b>Maria S.</b><span>RV Owner · Sedona, AZ</span></div></div></div>
      <div class="rev"><div class="stars">★★★★★</div><p>"Our kids still talk about the camper van trip through Idaho. Pickup was easy, the owner walked us through everything, and support was one call away the whole trip."</p><div class="who"><span class="avatar"></span><div><b>Chris &amp; Dana P.</b><span>Renters · Boise, ID</span></div></div></div>
    </div>
  </div>
</section>

<section class="faq">
  <div class="wrap">
    <div class="center"><span class="eyebrow">Good to know</span>
    <h2 class="sec-title">Frequently Asked Questions</h2></div>
    <div class="faq-list">
      <div class="faq-item">How is Zandoprik different from other RV rental sites?<svg width="8" height="5" viewBox="0 0 8 5"><path d="M.5.5l3.5 3.5 3.5-3.5" fill="none" stroke="#888"/></svg></div>
      <div class="faq-item">Is my trip protected if something goes wrong?<svg width="8" height="5" viewBox="0 0 8 5"><path d="M.5.5l3.5 3.5 3.5-3.5" fill="none" stroke="#888"/></svg></div>
      <div class="faq-item">Do I need RV experience to rent one?<svg width="8" height="5" viewBox="0 0 8 5"><path d="M.5.5l3.5 3.5 3.5-3.5" fill="none" stroke="#888"/></svg></div>
      <div class="faq-item">How much does it cost to list my RV?<svg width="8" height="5" viewBox="0 0 8 5"><path d="M.5.5l3.5 3.5 3.5-3.5" fill="none" stroke="#888"/></svg></div>
      <div class="faq-item">Can I set my own pricing and availability?<svg width="8" height="5" viewBox="0 0 8 5"><path d="M.5.5l3.5 3.5 3.5-3.5" fill="none" stroke="#888"/></svg></div>
      <div class="faq-item">What areas does Zandoprik cover?<svg width="8" height="5" viewBox="0 0 8 5"><path d="M.5.5l3.5 3.5 3.5-3.5" fill="none" stroke="#888"/></svg></div>
    </div>
  </div>
</section>

<section class="cta" role="img" aria-label="Dim evening backdrop of a forest campsite with a parked RV">
  <h2>The Open Road Is Calling. Answer It.</h2>
  <p>Join the growing pack of renters and owners who'd rather keep their money than hand it to a commission-hungry middleman.</p>
  <div class="btns"><span class="btn btn-green">Find An RV</span><span class="btn btn-ghost">List Your RV</span></div>
</section>

<footer>
  <div class="wrap">
    <div class="foot-top">
      <div class="foot-brand">
        <div class="logo">Zandoprik.com</div>
        <p>The flat-fee, peer-to-peer marketplace built for RV owners and the travelers who rent from them.</p>
        <div class="socials"><i></i><i></i><i></i><i></i></div>
      </div>
      <div class="foot-col"><h5>Company</h5><a>How It Works</a><a>Why Zandoprik</a><a>Reviews</a><a>FAQ</a></div>
      <div class="foot-col"><h5>For Renters</h5><a>Find an RV</a><a>RV Types</a><a>Trust &amp; Safety</a><a>Support</a></div>
      <div class="foot-col"><h5>For Owners</h5><a>List Your RV</a><a>Owner Earnings</a><a>Protection Plan</a><a>Owner Resources</a></div>
      <div class="news"><h5>Stay in the loop</h5><p>Road-trip tips and new owner listings, straight to your inbox.</p><div class="form"><span>you@example.com</span><b>Subscribe</b></div></div>
    </div>
    <div class="foot-bottom"><span>© 2026 Zandoprik.com. All rights reserved.</span><div><span>Terms of Service</span><span>Privacy Policy</span><span>Cookie Policy</span></div></div>
  </div>
</footer>

</body>
</html>
```